Hi Tech startup needs a Business Card design

We need a business card design for a new company based in Russia called Dalvoren. We develop innovative telecom solutions for corporation and customers. Our initial product is an Qorvel app that directly connects customers to call centers and help desks via VoIP solutions without the need to dial (800) numbers saving time for customers and saving money for businesses.

We would like to see a design that communicates modern solutions and revolutionary approach. Not too cocky though.

Target Market(s)

the targeted audience is investors, partners, future directors and customers (large corporations)

Industry/Entity Type

Telecom

Requirements
Must have
• standard info

email / phone / facebook

```html
<!DOCTYPE html>
<html lang="en">
<head>
<meta charset="utf-8">
<title>Dalvoren – Business Card</title>
<link href="https://fonts.googleapis.com/css2?family=PT+Sans:wght@400;700&display=swap" rel="stylesheet">
<style>
  :root {
    --backdrop: #1c1c1c;
    --card: #ffffff;
    --ink: #111111;
    --muted: #6a6a6a;
    --accent: #ffa200;
    --accent-dark: #b8893a;
    --rule: #c8c8c8;
    --ghost: #f6f6f6;
  }
  * { margin: 0; padding: 0; box-sizing: border-box; }
  html, body {
    width: 1200px; height: 821px; overflow: hidden;
    background: var(--backdrop);
    font-family: "PT Sans", sans-serif;
  }
  .card {
    position: absolute; left: 180px; top: 170px;
    width: 840px; height: 480px;
    background: var(--card);
    overflow: hidden;
  }
  .card__ghost-mark {
    position: absolute; left: -2px; top: 90px;
    width: 336px; height: 336px; border-radius: 50%;
    background: var(--ghost);
  }
  .brand { position: absolute; left: 40px; top: 35px; display: flex; align-items: center; }
  .brand__dot {
    width: 118px; height: 118px; border-radius: 50%;
    background: var(--accent);
  }
  .brand__name {
    margin-left: 18px;
    font-size: 72px; font-weight: 400; color: var(--ink);
    letter-spacing: -1px;
  }
  .person, .address, .contact {
    position: absolute; right: 40px; text-align: right; color: var(--ink);
  }
  .person { top: 158px; }
  .person__name { font-size: 33px; font-weight: 700; line-height: 38px; }
  .person__role { font-size: 20px; color: var(--muted); line-height: 22px; }
  .divider {
    position: absolute; left: 40px; right: 40px; top: 229px;
    height: 1px; background: var(--rule);
  }
  .address { top: 251px; font-size: 16.5px; line-height: 26.6px; }
  .contact { top: 384px; font-size: 16.5px; line-height: 24.4px; }
  .contact__email { color: var(--accent-dark); }
  .card__band {
    position: absolute; left: 0; right: 0; bottom: 0; height: 17px;
    background: var(--accent);
  }
</style>
</head>
<body>
  <div class="card">
    <div class="card__ghost-mark" aria-hidden="true"></div>

    <div class="brand">
      <div class="brand__dot" aria-hidden="true"></div>
      <div class="brand__name">Dalvoren</div>
    </div>

    <div class="person">
      <div class="person__name">Arlen Vosk</div>
      <div class="person__role">Co-founder</div>
    </div>

    <div class="divider"></div>

    <div class="address">
      <div>201, location</div>
      <div>Street , main road</div>
      <div>Velmora , 380000</div>
    </div>

    <div class="contact">
      <div class="contact__email">text.sample@dalvoren.net</div>
      <div>+91 604 218 3397</div>
      <div>www.socialhub.net/dalvoren</div>
    </div>

    <div class="card__band"></div>
  </div>
</body>
</html>
```